" Profissional liberal engenheiro civil, desenvolvo projetos de instalações elétricas e hidrossanitárias, projetos estruturais. Consultorias. Laudos Técnicos. "

```html
<!DOCTYPE html>
<html lang="pt-BR">
<head>
<meta charset="UTF-8">
<title>Cartão de Visitas</title>
<link href="https://fonts.googleapis.com/css2?family=Montserrat:wght@300;400;500;700;800&family=Roboto:wght@400&display=swap" rel="stylesheet">
<style>
  :root {
    --board: #a6a6a6;
    --navy: #0f1b27;
    --navy-line: #1c2a38;
    --blue: #2f8fd8;
    --blue-deep: #1f6fb2;
    --white: #ffffff;
    --ink: #1d2a36;
    --grey-text: #4a4f55;
    --label: #2b2b2b;
  }
  * { box-sizing: border-box; margin: 0; padding: 0; }
  html, body { width: 1200px; height: 1200px; overflow: hidden; }
  body {
    background: var(--board);
    font-family: "Montserrat", sans-serif;
    position: relative;
  }
  .board-label {
    position: absolute;
    left: 30px; top: 70px;
    font-family: "Roboto", sans-serif;
    font-size: 24px;
    letter-spacing: 0.5px;
    color: var(--label);
  }
  .card {
    position: absolute;
    overflow: hidden;
  }
  .card-front {
    left: 72px; top: 432px;
    width: 463px; height: 228px;
    background: var(--navy);
  }
  .card-back {
    left: 607px; top: 456px;
    width: 478px; height: 276px;
    background: var(--white);
  }
  .card-stripe {
    position: absolute; left: 0; right: 0; bottom: 0;
    height: 12px;
  }
  .card-stripe .thin {
    position: absolute; left: 0; right: 0; bottom: 0; height: 3px;
    background: var(--blue-deep);
  }
  .card-stripe .band {
    position: absolute; left: 12%; right: 0; bottom: 0; height: 10px;
    background: var(--blue);
    clip-path: polygon(3% 0, 100% 0, 100% 100%, 0 100%);
  }
  .identity {
    position: absolute;
    display: flex; align-items: center; gap: 14px;
  }
  .card-front .identity { left: 36px; top: 78px; }
  .card-back .identity { left: 150px; top: 58px; gap: 12px; }
  .identity-mark {
    width: 30px; height: 30px; background: var(--blue); flex: none;
  }
  .card-back .identity-mark { width: 26px; height: 26px; }
  .identity-name {
    font-size: 27px; line-height: 1; white-space: nowrap;
  }
  .card-front .identity-name { color: var(--white); }
  .card-back .identity-name { color: var(--ink); font-size: 24px; }
  .identity-name b { font-weight: 800; }
  .identity-name span { font-weight: 400; }
  .identity-role {
    margin-top: 6px;
    font-size: 9.5px; font-weight: 500;
    letter-spacing: 6.2px;
  }
  .card-front .identity-role { color: #c9d4de; }
  .card-back .identity-role { color: var(--grey-text); font-size: 8.5px; letter-spacing: 5.4px; }
  .contact-list {
    position: absolute; right: 20px; top: 118px;
    list-style: none;
    font-size: 11px; color: var(--grey-text);
    text-align: right;
  }
  .contact-list li {
    display: flex; justify-content: flex-end; align-items: center; gap: 12px;
    height: 22px;
  }
  .contact-list li.address { height: auto; margin-top: 6px; align-items: flex-start; line-height: 1.35; }
  .contact-list svg { width: 11px; height: 11px; flex: none; fill: var(--blue); }
</style>
</head>
<body>
  <p class="board-label">CARTÃO DE VISITAS</p>

  <section class="card card-front">
    <div class="identity">
      <div class="identity-mark"></div>
      <div>
        <p class="identity-name"><b>RAFAEL</b> <span>MONTEIRO</span></p>
        <p class="identity-role">ENGENHEIRO CIVIL</p>
      </div>
    </div>
    <div class="card-stripe"><div class="band"></div><div class="thin"></div></div>
  </section>

  <section class="card card-back">
    <div class="identity">
      <div class="identity-mark"></div>
      <div>
        <p class="identity-name"><b>RAFAEL</b> <span>MONTEIRO</span></p>
        <p class="identity-role">ENGENHEIRO CIVIL</p>
      </div>
    </div>
    <ul class="contact-list">
      <li>(00) 00000.0000 / 00000.0000
        <svg viewBox="0 0 24 24"><path d="M6.6 10.8a15.1 15.1 0 0 0 6.6 6.6l2.2-2.2a1 1 0 0 1 1-.25 11.4 11.4 0 0 0 3.6.57 1 1 0 0 1 1 1V20a1 1 0 0 1-1 1A17 17 0 0 1 3 4a1 1 0 0 1 1-1h3.5a1 1 0 0 1 1 1c0 1.25.2 2.45.57 3.57a1 1 0 0 1-.25 1z"/></svg>
      </li>
      <li>contato@exemplo.com.br
        <svg viewBox="0 0 24 24"><path d="M2 5h20v14H2z M4 7v.5l8 5 8-5V7z" fill-rule="evenodd"/></svg>
      </li>
      <li>www.exemplo.com.br
        <svg viewBox="0 0 24 24"><path d="M2 4h20v13H2zM4 6v9h16V6zM8 19h8v2H8z" fill-rule="evenodd"/></svg>
      </li>
      <li class="address"><span>End. completo, 00, Bairro<br>CEP 0000.0000 - Cidade-SP</span>
        <svg viewBox="0 0 24 24"><path d="M12 2a7 7 0 0 0-7 7c0 5.2 7 13 7 13s7-7.8 7-13a7 7 0 0 0-7-7zm0 9.5a2.5 2.5 0 1 1 0-5 2.5 2.5 0 0 1 0 5z"/></svg>
      </li>
    </ul>
    <div class="card-stripe"><div class="band"></div><div class="thin"></div></div>
  </section>
</body>
</html>
```